KVT Roofing Pty Ltd

We are a high end residential Roofing company
We would like something silimar to the attached logo with the same color scheme

Target Market(s)

High end residential Builders & Architects

Industry/Entity Type

Residential

```html
<!DOCTYPE html>
<html lang="en">
<head>
<meta charset="utf-8">
<title>KVT Roofing Pty Ltd – Business Card</title>
<link rel="stylesheet" href="https://fonts.googleapis.com/css2?family=PT+Sans:wght@400;700&family=PT+Sans+Narrow&display=swap">
<style>
  :root{
    --stage-light:#e9eaeb;
    --stage-dark:#b9bbbd;
    --card-white:#ffffff;
    --slate:#2b3741;
    --slate-tile:#45535f;
    --brand-blue:#1e9ad3;
    --roof-blue:#cfe0ee;
    --ink:#111a22;
    --ink-soft:#4a5863;
    --heading-grey:#3e4d59;
  }
  *{margin:0;padding:0;box-sizing:border-box}
  html,body{width:1200px;height:1200px;overflow:hidden}
  body{
    background:radial-gradient(circle at 50% 45%,var(--stage-light) 0%,var(--stage-dark) 100%);
    font-family:"PT Sans",sans-serif;
    position:relative;
  }
  .card{position:absolute;left:216px;width:766px;height:462px;overflow:hidden}
  .card--front{top:132px;background:var(--card-white)}
  .card--back{top:604px;background:var(--slate)}
  .card__art{position:absolute;inset:0;width:100%;height:100%}

  .company-name{position:absolute;font-weight:400;letter-spacing:-0.5px;white-space:nowrap}
  .company-name__initials{color:var(--brand-blue);font-weight:700}
  .card--front .company-name{left:40px;top:100px;font-size:41px;color:var(--heading-grey)}

  .partner-mark{position:absolute;left:481px;top:30px;width:198px;text-align:center}
  .partner-mark__square{width:198px;height:152px;background:var(--slate-tile)}
  .partner-mark__name{display:block;margin-top:12px;font-size:27px;color:var(--heading-grey);letter-spacing:.5px;white-space:nowrap}

  .person{position:absolute;left:40px;top:244px}
  .person__name{font-size:29px;font-weight:700;color:var(--ink);line-height:1.1}
  .person__role{font-size:21px;color:var(--ink-soft);margin-top:2px}

  .contact{position:absolute;left:250px;top:312px;list-style:none}
  .contact__item{display:flex;align-items:center;height:31px;font-size:23px;color:var(--ink);white-space:nowrap}
  .contact__icon{width:17px;height:17px;margin-right:12px;flex:none}

  .back-pattern{position:absolute;inset:0;background:linear-gradient(180deg,#2e3b46 0%,#28343e 100%)}
  .back-tile{position:absolute;left:474px;top:240px;width:119px;height:100px;background:var(--slate-tile)}
  .card--back .company-name{right:26px;top:362px;font-size:50px;color:var(--card-white)}
</style>
</head>
<body>

<section class="card card--front">
  <svg class="card__art" viewBox="0 0 638 385" preserveAspectRatio="none" aria-hidden="true">
    <polygon points="0,235 163,128 638,350 620,350 163,196 0,268" fill="var(--roof-blue)"/>
    <polygon points="0,335 185,335 193,348 0,348" fill="var(--brand-blue)"/>
    <rect x="0" y="352" width="638" height="33" fill="var(--slate)"/>
  </svg>

  <h1 class="company-name"><span class="company-name__initials">KVT</span> Roofing Pty Ltd</h1>

  <div class="partner-mark">
    <div class="partner-mark__square"></div>
    <span class="partner-mark__name">Ridgeline Build</span>
  </div>

  <div class="person">
    <p class="person__name">Corin Maddox</p>
    <p class="person__role">General Manager</p>
  </div>

  <ul class="contact">
    <li class="contact__item">
      <svg class="contact__icon" viewBox="0 0 16 16" aria-hidden="true"><rect width="16" height="16" fill="var(--brand-blue)"/><path d="M4 4.5c1-1 1.8-.6 2.3.4l.4.9c.2.5-.1.9-.5 1.2.5 1 1.2 1.7 2.2 2.2.3-.4.7-.7 1.2-.5l.9.4c1 .5 1.4 1.3.4 2.3-2.8 1.2-7.9-3.9-6.9-6.9z" fill="#fff"/></svg>
      0400 318 625
    </li>
    <li class="contact__item">
      <svg class="contact__icon" viewBox="0 0 16 16" aria-hidden="true"><rect width="16" height="16" fill="var(--brand-blue)"/><path d="M8 3.5 2.8 8h1.6v4.5h2.6V10h2v2.5h2.6V8h1.6z" fill="#fff"/></svg>
      218 Harbour Street, Port Ashford
    </li>
    <li class="contact__item">
      <svg class="contact__icon" viewBox="0 0 16 16" aria-hidden="true"><rect width="16" height="16" fill="var(--brand-blue)"/><rect x="3" y="4.5" width="10" height="7" fill="#fff"/><path d="M3 4.5 8 8.5l5-4" fill="none" stroke="var(--brand-blue)" stroke-width="1"/></svg>
      cmaddox@kvtsteelroofing.com.au
    </li>
  </ul>
</section>

<section class="card card--back">
  <div class="back-pattern" role="img" aria-label="Faint repeating grid of brand tiles across the slate background"></div>
  <div class="back-tile"></div>
  <h2 class="company-name"><span class="company-name__initials">KVT</span> Roofing Pty Ltd</h2>
</section>

</body>
</html>
```